Training Course Outline

tovo-craft (tovo-craft.com) is a Training & Development company in the Middle East. We offer a number of corporate training courses and leadership development programmes.
We need an A4, colour, double-sided, flyer template that we will edit and use to advertise/outline our courses/programmes (1 double-sided A4 flyer for each course/programme).

*****LATEST UPDATE - WEDNESDAY 5TH DECEMBER********

We've had some fantastic designs submitted which have helped us refine our ideas about what the final flyer will look like.

Please refer to file 6, an attached image called updated design brief. This is our unqualified mock up pulled together from the designs we like so far using Paint...

We'd like to see revised designs which use this as a template. It retains our existing brand look and feel from the other attached brochures (see files 2 and 5 attached). But, the middle section (Training Methodology) on the back page still requires some design work, we're open to ideas here. The text sections (About us, Prog objectives, Contact us, Who should attend, Program outline) are all positioned as we'd like them but open to design input in terms of look and feel, perhaps background color which isnt as harsh as plain white.

We'll only be considering designs that follow this layout from here on in.

Thanks again for your input and patience; feel free to ask if you have any questions.

:-)
Updates

:-)

Reason: At this stage, unfortunately none of the submitted designs are exactly what we're looking for. Whilst we've had some great designs, given the latest update we've provided, we'd like to give designers some more time to submit designs in line with these requirements. Please take a look at the most recent feedback and attachment for guidance on what we're looking for.

Please use the tovo-craft colour theme of;
 
#F3912D 
#FCBD1B 
#B12009 
#571D00 

For a visual aid, check File 3 in the brief.

Thanks!

Target Market(s)

Corporate clients willing to outsource and invest in external training providers.

Industry/Entity Type

Leadership

Requirements
Must have
• The brochure must be 1 A4, colour & double-sided.
It must use the tovo-craft & brand promise logo.
It must use the tovo-craft colour theme;
Pantone : Orange 021 C
CMYK: C-0 / M-70 / Y-100 / K-0
RGB: R-246 / G-124 / B-27
Electronic: Hex # F67C1B
It must include Social Media;
Twitter: tovohubgulf
Facebook: tovohub
YouTube: tovohubTV
LinkedIn: tovo-hub FZ LLC
Blog: tovo-hub.ae/blog
Must include tovo-craft tag line: Lifting Team Output With Coaching and Growth
Must use Font: Rotis SanSerif AT Light
Must include the following sections (included example text);
1. About tovo-craft;
tovo-craft has worked with hundreds of leading Middle East companies to provide measurable training & development programmes, spanning more than 19 years in the region.  Founded in Dubai, with a comprehensive understanding of the cultural and business needs, the whole team of tovo-craft is passionate about performance!
2. Contact Us;
www.tovo-craft.com
info@tovo-craft.com
Dubai
PO Box 58176
United Arab Emirates
+971 (0)4 267 8352
Abu Dhabi
PO Box 146827
United Arab Emirates
+971 (0)2 318 5769
3. Intro;
The QRP Steward Pathway is tailored to meet your organisation’s specific needs with relevant case studies and
exercises in line with our design guarantee.

4. Programme Overview;
What makes the tovo-craft Steward Pathway Different?

Our focus in on delivering sustainable and measurable improvement in the performance of your managers and supervisors by enhancing their leadership capabilities. To do this we adhere to three principles:

a. Tailored Content
We spend time with your organisation to understand the issues and design the programme so that the Steward Pathway takes specific account of your company values, performance management system and ways of working (policies and procedures).

b. Assessment and Coaching
Our process provides assessment, support and feedback throughout the Journey including:
* One to One coaching with an QRP accredited coach
* End of stage 1 evaluation gate
* Learning sets
* Learning logs

c. Tangible Business Results
We focus on providing the measurable return on investment for leadership training
5. Course Content:
(use tables to summarise the course content, see attached example)
6. Programme outcomes:
Measurable Performance Results
* Final 180° Survey (Optional)
* Particpant learning logs submitted for evaluation
* tovo-craft assessment
* QRP adjudicator assessment
* Report on results and assignment measures
7. Testimonial quote;
"This programme literally changed the lives of senior management within our organisation" - Editor, Publishing Company, Dubai
8. Programme/Course Name/Title
Nice to have
• Clickable PDF with live links to our social media channels, website & email.
Copyrite logo & text at the bottom of both pages as follows;
© 2012 tovo-craft - A subsidiary of tovo-hub FZ LLC
Should not have
• Do not use colours or fonts outside of the provided themes.
Do not use non-corporate images (no cartoon images).

```html
<!DOCTYPE html>
<html lang="en">
<head>
<meta charset="utf-8">
<title>QRP Steward Pathway – Course Outline</title>
<link href="https://fonts.googleapis.com/css2?family=Hind:wght@300;400&display=swap" rel="stylesheet">
<style>
  :root {
    --orange: #f67c1b;
    --orange-light: #f79a45;
    --amber: #fcbd1b;
    --red: #b12009;
    --brown: #571d00;
    --paper: #ffffff;
    --ink: #2a2a2a;
    --body: #666666;
    --photo-office: #8a8f94;
    --photo-hands: #9a9a9a;
  }
  * { margin: 0; padding: 0; box-sizing: border-box; }
  html, body { width: 1200px; height: 848px; overflow: hidden; background: var(--paper); }
  body { font-family: "Hind", Arial, sans-serif; font-weight: 300; }
  .spread { position: relative; width: 1200px; height: 848px; }

  .page-inner { position: absolute; left: 0; top: 0; width: 596px; height: 848px; background: var(--paper); border-right: 1px solid #d9d9d9; }
  .page-outer {
    position: absolute; left: 596px; top: 0; width: 604px; height: 848px;
    background: linear-gradient(180deg, var(--orange-light) 0%, var(--orange) 26%, var(--orange) 100%);
  }

  .block { position: absolute; font-size: 13px; line-height: 18px; }
  .block h2 { font-size: 16.5px; font-weight: 400; line-height: 20px; }
  .block p { margin: 0; }
  .page-inner .block h2 { color: var(--ink); }
  .page-inner .block { color: var(--body); }
  .page-outer .block, .page-outer .block h2 { color: var(--paper); }
  .gap { height: 18px; }
  .small { font-size: 11px; line-height: 15px; }

  .promise-mark { position: absolute; left: 32px; top: 150px; display: flex; align-items: center; gap: 6px; }
  .promise-mark .dot { width: 18px; height: 18px; border-radius: 50%; background: var(--orange); }
  .promise-mark .name { font-size: 17px; font-weight: 400; color: var(--orange); }

  .photo-team {
    position: absolute; left: 105px; top: 223px; width: 491px; height: 194px;
    background: linear-gradient(180deg, #cfd6da 0%, var(--photo-office) 55%, #4a4c4f 100%);
  }
  .band { position: absolute; top: 223px; height: 194px; }
  .band-amber { left: 596px; width: 57px; background: var(--amber); }
  .band-red { left: 653px; width: 61px; background: var(--red); }
  .band-brown { left: 714px; width: 59px; background: #6b0a06; }
  .photo-hands {
    position: absolute; left: 773px; top: 223px; width: 418px; height: 194px;
    background: linear-gradient(90deg, #5a5a5a 0%, var(--photo-hands) 45%, #dcdcdc 60%, #3c3c3c 100%);
  }
</style>
</head>
<body>
<div class="spread">
  <section class="page-inner">
    <div class="promise-mark"><span class="dot"></span><span class="name">tovo-craft</span></div>

    <div class="block" style="left:170px; top:83px; width:380px;">
      <h2>Intro</h2>
      <p>The QRP Steward Pathway is tailored to meet your organisation’s specific needs with relevant case studies and exercises in line with our design guarantee.</p>
    </div>

    <div class="photo-team" role="img" aria-label="Photo of business team meeting by a bright office window"></div>

    <div class="block" style="left:170px; top:442px; width:370px;">
      <h2>Programme Overview</h2>
      <p>What makes the tovo-craft Steward Pathway Different?</p>
      <div class="gap"></div>
      <p>Our focus in on delivering sustainable and measurable improvement in the performance of your managers and supervisors by enhancing their leadership capabilities. To do this we adhere to three principles:</p>
      <div class="gap"></div>
      <h2>a. Tailored Content</h2>
      <p>We spend time with your organisation to understand the issues and design the programme so that the Steward Pathway takes specific account of your company values, performance management system and ways of working (policies and procedures).</p>
    </div>
  </section>

  <section class="page-outer"></section>

  <div class="block" style="left:724px; top:83px; width:380px;">
    <h2>b. Assessment and Coaching</h2>
    <p>Our process provides assessment, support and feedback throughout the Journey including:</p>
    <p>* One to One coaching with an QRP accredited coach</p>
    <p>* End of stage 1 evaluation gate</p>
    <p>* Learning sets</p>
    <p>* Learning logs</p>
  </div>

  <div class="band band-amber"></div>
  <div class="band band-red"></div>
  <div class="band band-brown"></div>
  <div class="photo-hands" role="img" aria-label="Black and white photo of hands joining two jigsaw puzzle pieces"></div>

  <div class="block" style="left:724px; top:442px; width:390px;">
    <h2>c. Tangible Business Results</h2>
    <p>We focus on providing the measurable return on investment for leadership training</p>
    <div class="gap"></div>
    <h2>Course Content:</h2>
    <p class="small">(use tables to summarise the course content, see attached example)</p>
    <div style="height:10px"></div>
    <h2>Programme outcomes:</h2>
    <p>Measurable Performance Results</p>
    <p>* Final 180° Survey (Optional)</p>
    <p>* Particpant learning logs submitted for evaluation</p>
    <p>* tovo-craft assessment</p>
    <p>* QRP adjudicator assessment</p>
    <p>* Report on results and assignment measures</p>
    <div style="height:10px"></div>
    <h2>Testimonial quote;</h2>
    <p>"This programme literally changed the lives of senior management within our organisation"</p>
    <p style="margin-top:3px">- Editor, Publishing Company, Dubai</p>
    <div style="height:8px"></div>
    <h2>Programme/Course Name/Title</h2>
  </div>
</div>
</body>
</html>
```